Birchline Septic Solutions

Would like to see some single sided ones but would also like to see some double sided with one sided only being the logo. Owners name is Tom Halvick. Phone number is 555-214-0387
Services are pumping, inspections, installs, and repairs

Contact Information for Business Card

555-241-0387 Tom Halvick Maple Ridge, OH

```html
<!DOCTYPE html>
<html lang="en">
<head>
<meta charset="utf-8">
<title>Birchline Septic Solutions – Business Cards</title>
<link rel="stylesheet" href="https://fonts.googleapis.com/css2?family=Montserrat:wght@400;500;600;800&display=swap">
<style>
  :root {
    --teal: #35aca6;
    --ink: #1c1c1c;
    --paper: #ffffff;
    --stage: #a9abaf;
    --muted: #3a3a3a;
  }
  * { margin: 0; padding: 0; box-sizing: border-box; }
  html, body { width: 1200px; height: 876px; overflow: hidden; }
  body {
    background: var(--stage);
    font-family: "Montserrat", sans-serif;
    display: flex;
    align-items: center;
    justify-content: center;
    gap: 44px;
  }
  .card {
    width: 520px;
    height: 297px;
    position: relative;
    border-radius: 3px;
    box-shadow: 0 10px 24px rgba(0,0,0,0.18);
  }
  .card--front { background: var(--paper); color: var(--ink); }
  .card--back {
    background: var(--teal);
    display: flex;
    align-items: center;
    justify-content: center;
  }
  .contact { position: absolute; left: 40px; top: 36px; }
  .contact__name {
    color: var(--teal);
    font-weight: 800;
    font-size: 25px;
    letter-spacing: 0.5px;
    text-transform: uppercase;
    line-height: 1;
  }
  .contact__role { font-size: 11px; font-weight: 500; margin-top: 5px; }
  .contact__list { list-style: none; margin-top: 14px; }
  .contact__item {
    display: flex; align-items: center; gap: 7px;
    font-size: 13px; font-weight: 500; color: var(--muted);
    margin-bottom: 6px; letter-spacing: 0.4px;
  }
  .contact__icon { width: 11px; height: 11px; fill: var(--teal); flex: none; }
  .services {
    position: absolute; left: 40px; right: 40px; bottom: 30px;
    font-size: 15px; font-weight: 600; letter-spacing: 1px;
    text-transform: uppercase;
    display: flex; gap: 9px; white-space: nowrap;
  }
  .services__sep { color: var(--teal); font-weight: 500; }
  .wordmark {
    font-weight: 800;
    text-transform: uppercase;
    text-align: center;
    line-height: 1.05;
  }
  .wordmark--front {
    position: absolute; right: 44px; top: 70px;
    color: var(--ink); font-size: 24px; letter-spacing: 1px;
  }
  .wordmark--back { color: var(--paper); font-size: 34px; letter-spacing: 1.5px; }
</style>
</head>
<body>
  <section class="card card--front" aria-label="Business card front">
    <div class="contact">
      <h1 class="contact__name">Tom Halvick</h1>
      <p class="contact__role">Owner</p>
      <ul class="contact__list">
        <li class="contact__item">
          <svg class="contact__icon" viewBox="0 0 24 24" aria-hidden="true"><path d="M6.6 10.8a15.2 15.2 0 0 0 6.6 6.6l2.2-2.2c.3-.3.7-.4 1-.2 1.1.4 2.3.6 3.6.6.6 0 1 .4 1 1V20c0 .6-.4 1-1 1A17 17 0 0 1 3 4c0-.6.4-1 1-1h3.5c.6 0 1 .4 1 1 0 1.3.2 2.5.6 3.6.1.3 0 .7-.2 1z"/></svg>
          555-214-0387
        </li>
        <li class="contact__item">
          <svg class="contact__icon" viewBox="0 0 24 24" aria-hidden="true"><path d="M12 2a7 7 0 0 0-7 7c0 5.2 7 13 7 13s7-7.8 7-13a7 7 0 0 0-7-7zm0 9.5A2.5 2.5 0 1 1 12 6.5a2.5 2.5 0 0 1 0 5z"/></svg>
          Maple Ridge, OH
        </li>
      </ul>
    </div>
    <p class="wordmark wordmark--front">Birchline<br>Septic<br>Solutions</p>
    <p class="services">
      <span>Pumping</span><span class="services__sep">|</span>
      <span>Inspections</span><span class="services__sep">|</span>
      <span>Installs</span><span class="services__sep">|</span>
      <span>Repairs</span>
    </p>
  </section>

  <section class="card card--back" aria-label="Business card back">
    <p class="wordmark wordmark--back">Birchline<br>Septic Solutions</p>
  </section>
</body>
</html>
```